Moder Business Card Design for Renewables Business

Need a business card design for my business. We collect & repurpose spent coffee ground from cafes. The cards will be made from recycled paper. Needs to fit our corporate colour scheme of white, green & brown (see logo for colour codes). Eco friendly, modern, intresting & eye catching.
This card needs to convey the message of the business and fit into its mantra of eco-friendly, sustainable etc.

Target Market(s)

Cafe Owners, Coffee Drinkers, Recycling Companies, Farmers

Industry/Entity Type

Recycling

Contact Information for Business Card

Name; Peter Halloran
Phone; 0412 386 527
e-mail; info@lumatrove.com.au
website; www.lumatrove.com.au

Font styles to use
Sans Serif
Script

Colors

Designer to choose colors to be used in the design.

Requirements
Must have
• FRONT;
• Logo, Name (Peter Halloran), phone number, e-mail address, website
• BACK;
• On the back in cursive text; 'SUSTAINABILITY IN THE DAILY GRIND'
• Small facebook & Instagram logos with text 'Lumatrove'
Should not have
• messy design

```html
<!DOCTYPE html>
<html lang="en">
<head>
<meta charset="utf-8">
<title>Lumatrove Business Card</title>
<link href="https://fonts.googleapis.com/css2?family=Open+Sans:wght@400;600;700&family=Pinyon+Script&display=swap" rel="stylesheet">
<style>
  :root {
    --backdrop: #1d1e21;
    --kraft: #b8997a;
    --kraft-dark: #a5866a;
    --leaf: #6b8f2c;
    --bean: #4a2a17;
    --ink: #5a3a24;
    --cream: #f1dcc6;
    --olive: #6f8a37;
    --roast: #4e2a12;
  }
  * { margin: 0; padding: 0; box-sizing: border-box; }
  html, body { width: 1200px; height: 1017px; overflow: hidden; }
  body {
    background: var(--backdrop);
    display: flex;
    align-items: center;
    justify-content: center;
    gap: 44px;
    font-family: "Open Sans", Arial, sans-serif;
  }
  .card {
    width: 532px;
    height: 304px;
    border-radius: 3px;
    position: relative;
    overflow: hidden;
    box-shadow: 0 14px 30px rgba(0,0,0,.45);
  }
  /* Front */
  .card-front {
    background: radial-gradient(ellipse at 40% 30%, #c4a687 0%, var(--kraft) 55%, var(--kraft-dark) 100%);
  }
  .brand {
    position: absolute;
    left: 38px;
    top: 120px;
    width: 120px;
    display: flex;
    flex-direction: column;
    align-items: center;
    gap: 10px;
  }
  .brand-dot {
    width: 82px;
    height: 82px;
    border-radius: 50%;
    border: 5px solid var(--bean);
  }
  .brand-name {
    font-weight: 600;
    font-size: 16px;
    letter-spacing: .5px;
    color: var(--leaf);
  }
  .divider {
    position: absolute;
    left: 176px;
    top: 112px;
    width: 1px;
    height: 104px;
    background: var(--leaf);
  }
  .contact {
    position: absolute;
    left: 198px;
    top: 106px;
    color: var(--ink);
  }
  .person {
    font-weight: 700;
    font-size: 18px;
    letter-spacing: .3px;
    color: var(--bean);
    margin-bottom: 10px;
  }
  .person .first { color: var(--leaf); }
  .contact-line {
    font-size: 12.5px;
    line-height: 22px;
    letter-spacing: .2px;
  }
  /* Back */
  .card-back {
    background: linear-gradient(150deg, var(--olive) 0%, #6a7a33 35%, #5e4320 70%, var(--roast) 100%);
  }
  .motto {
    position: absolute;
    left: 0; right: 0;
    top: 62px;
    text-align: center;
    font-family: "Pinyon Script", cursive;
    font-size: 46px;
    line-height: 52px;
    color: var(--cream);
  }
  .social {
    position: absolute;
    right: 18px;
    bottom: 16px;
    display: flex;
    align-items: center;
    gap: 6px;
    font-size: 12px;
    color: var(--cream);
  }
  .social-mark {
    width: 10px;
    height: 10px;
    border: 1px solid var(--cream);
  }
</style>
</head>
<body>
  <section class="card card-front">
    <div class="brand">
      <div class="brand-dot"></div>
      <div class="brand-name">LUMATROVE</div>
    </div>
    <div class="divider"></div>
    <div class="contact">
      <p class="person"><span class="first">PETER</span> HALLORAN</p>
      <p class="contact-line">P: 0412 386 527</p>
      <p class="contact-line">E: info@lumatrove.com.au</p>
      <p class="contact-line">W: www.lumatrove.com.au</p>
    </div>
  </section>

  <section class="card card-back">
    <p class="motto">Sustainability<br>in the<br>daily grind</p>
    <div class="social">
      <span class="social-mark"></span>
      <span>Lumatrove</span>
    </div>
  </section>
</body>
</html>
```